eye catching frozen pies package

We are looking for package design for our new product “Tart ZIP”, we are food production start-up based in west Canada 'Marlo Food'. Our product it is basically a healthy and natural type of pie that we are willing to retail it in local groceries.
We are mainly marketing the Tart ZIP being far better healthy choice for traditional pies, as our product has no yeast or baking additives, has no oil, no eggs, and it’s baked.
Tart ZIP has Mediterranean origins but we had tweaked it to fit the Canadian consumers, and that's one of the product main strong marketing points. Tart ZIP comes in 3 types (Beef, Veggie, and Cheese).

We have picked Block Bottom Stand up Pouch as package (see attachment 09-13) with both sides made of semi-transparent material (matte), bag size is (attachment 08) Width 230 mm x Length 170 x Bottom gusset 100 mm. Each bag will contain 6 pieces of Tart ZIP (net weight 540 gr), stacked like a cylinder/tube. the reason why we choose this bag because we wanted the pack to look like a box while it is simple bag only, and that's why we need the art design of the back to reflect the simple product in a very attractive/eye catching concept. The bag front will face the consumer when it is inside the display freezers and to grab their eyes by its shape, thus the design on the bag shall get use of the bag shape and exposure.

Note: all product photos are in JPG format but RAW/PDF are available for the final design stage, and all photos need some Photoshop for colour/light correction (design is responsible to create the best photo file)

Target Market(s)

Tart ZIP is ready to eat and our customers are young working couples/moms, kids lunch boxes, and healthy lite meals seekers. We believe that Tart ZIP is a very new product in our market and there is no directly similar product.

Industry/Entity Type

Product

Font styles to use
Serif
Sans Serif

Colors
9bcb3c
ffffff
e8e8e8
d9d9d9
000000

Requirements
Must have
• Deliverable:
• • Stand up pouch overall design
• • Product name label design
• • Back side label design (nutrition facts and ingredients)
• Front of pack:
• • Brand name: Tart ZIP
• • Common Name: Home-style Baked Pies
• • Product name: red for BEEF, green for VEGGIE, yellow for CHEESE (circular sticker/label to identify which type of tart zip with unique colour for each type)
• • From Canadian nature to your table (with Canadian maple leaf logo)
• • No egg, No Shortening, No yeast, No Preservatives.
• • Photo and art works
• • 6 pieces
• • Cooking instruction: 2 min microwave (graphical representation)
• Back of pack:
• • Portion of the back shall be left blank to receive white sticker/label that contains
• o Nutrition facts: use attached table (will be shared later)
• o Ingredients: see attachment A
• o Allergies : contains wheat, dairy, sesame seeds, soy sauce
• o Net Weight: 560 g
• o Best before: (leave empty space for stamp)
• o Contacts: Marlo Food Ltd., T4R 2W8, AB, Canada
• o Marlo Food logo: see attachment B
• o 587 555 0183 – marlofoodservices@brindlemail.example
Nice to have
• Design style:
• We prefer modern to contemprory design style with range of colors similar to the attached (lime green, white, light grey) but it is up to the designer to suggest any other styles or/and colors, as we are strongly open to new ideas.
Should not have
• design should not use any of the attached bags photo designs (attachments 08-13)

```html
<!DOCTYPE html>
<html lang="en">
<head>
<meta charset="utf-8">
<title>Tart ZIP – Home-Style Baked Pies Pack Front</title>
<link href="https://fonts.googleapis.com/css2?family=Amatic+SC:wght@700&family=Nunito:wght@800;900&family=Special+Elite&display=swap" rel="stylesheet">
<style>
  :root {
    --brand-green: #35a84a;
    --deep-green: #1f8b3b;
    --lime: #9bcb3c;
    --white: #ffffff;
    --marble-light: #f4f4f4;
    --marble-mid: #e8e8e8;
    --marble-grey: #d9d9d9;
    --crust-light: #f1e3bd;
    --crust-dark: #d8bd7f;
    --stamp-red: #a3262b;
    --ink: #000000;
  }
  * { margin: 0; padding: 0; box-sizing: border-box; }
  html, body { width: 1200px; height: 810px; overflow: hidden; background: var(--white); }
  .canvas { position: relative; width: 1200px; height: 810px; background: var(--white); }

  .pack-front {
    position: absolute; left: 106px; top: 42px; width: 982px; height: 726px;
    overflow: hidden;
  }
  .marble-backdrop {
    position: absolute; inset: 0;
    background: linear-gradient(160deg, var(--marble-light) 0%, var(--white) 40%, var(--marble-mid) 75%, var(--marble-light) 100%);
  }
  .green-panel { position: absolute; inset: 0; width: 982px; height: 726px; }

  .product-photo {
    position: absolute; left: 342px; top: 322px; width: 620px; height: 304px;
    background: radial-gradient(ellipse at 80% 50%, var(--crust-light) 0%, var(--crust-dark) 70%, transparent 71%),
                linear-gradient(90deg, var(--crust-light), var(--crust-dark) 50%, var(--crust-light));
    border-radius: 60px 150px 150px 60px;
    opacity: .9;
  }

  .brand-name {
    position: absolute; left: 0; top: 118px; width: 982px; padding-left: 130px;
    text-align: center;
    font-family: "Nunito", sans-serif; font-weight: 900; font-size: 122px;
    color: var(--brand-green); line-height: 1; letter-spacing: -1px;
  }
  .brand-swoosh { position: absolute; left: 274px; top: 232px; width: 500px; height: 64px; }
  .common-name {
    position: absolute; left: 362px; top: 294px;
    font-family: "Amatic SC", sans-serif; font-weight: 700; font-size: 42px;
    color: var(--deep-green); transform: rotate(-5deg); transform-origin: left top;
    letter-spacing: 0.5px; line-height: 1; white-space: nowrap;
  }

  .variety-badge { position: absolute; left: 802px; top: 150px; width: 140px; height: 140px; }
  .variety-badge-text {
    position: absolute; left: 802px; top: 150px; width: 140px; height: 140px;
    display: flex; align-items: center; justify-content: center;
    font-family: "Amatic SC", sans-serif; font-weight: 700; font-size: 40px;
    color: var(--lime); transform: rotate(-8deg);
  }

  .claims { position: absolute; left: 30px; top: 330px; list-style: none; }
  .claim {
    display: flex; align-items: center; gap: 8px; height: 44px;
    font-family: "Amatic SC", sans-serif; font-weight: 700; font-size: 42px;
    color: var(--white); line-height: 1;
  }
  .claim-tick { width: 34px; height: 30px; flex: none; }

  .origin-stamp {
    position: absolute; left: 48px; top: 550px; width: 322px; height: 96px;
    border: 3px solid var(--stamp-red); transform: rotate(-7deg);
    display: flex; align-items: center; gap: 14px; padding-left: 18px;
  }
  .origin-leaf { width: 58px; height: 58px; background: var(--stamp-red); opacity: .85; border-radius: 4px; flex: none; }
  .origin-text {
    font-family: "Special Elite", serif; font-size: 19px; line-height: 1.15;
    color: var(--stamp-red); text-transform: uppercase; white-space: nowrap;
  }

  .info-band { position: absolute; left: 0; top: 654px; width: 982px; height: 72px; }
  .cook-time { position: absolute; left: 323px; top: 16px; display: flex; align-items: center; gap: 12px; }
  .microwave-icon { width: 54px; height: 36px; }
  .cook-minutes {
    font-family: "Nunito", sans-serif; font-weight: 900; font-size: 50px; color: var(--white); line-height: 1;
  }
  .cook-label {
    font-family: "Nunito", sans-serif; font-weight: 800; font-size: 19px; color: var(--white); line-height: 1.05;
  }
  .piece-count {
    position: absolute; right: 32px; top: 14px;
    font-family: "Nunito", sans-serif; font-weight: 900; font-size: 28px; color: var(--white);
  }
  .piece-count strong { font-size: 42px; }
</style>
</head>
<body>
<div class="canvas">
  <section class="pack-front">
    <div class="marble-backdrop" role="img" aria-label="White marble surface background"></div>

    <svg class="green-panel" viewBox="0 0 982 726" role="img" aria-label="Green panel with line drawings of vegetables">
      <path d="M0 0 H262 C240 110 320 200 300 330 C284 440 318 560 294 654 H982 V726 H0 Z" fill="var(--brand-green)"/>
    </svg>

    <div class="product-photo" role="img" aria-label="Photo of four golden baked rolled pies, three standing in a row and one showing its spiral top"></div>

    <h1 class="brand-name">Tart ZIP</h1>
    <svg class="brand-swoosh" viewBox="0 0 500 64" aria-hidden="true">
      <path d="M0 62 C160 36 330 18 498 2 C330 24 170 44 0 64 Z" fill="var(--brand-green)"/>
    </svg>
    <p class="common-name">HOME-STYLE BAKED PIES</p>

    <svg class="variety-badge" viewBox="0 0 140 140" aria-hidden="true">
      <polygon fill="var(--lime)" points="70,2 79,15 94,6 98,22 115,18 113,34 129,37 121,51 136,59 124,70 136,81 121,89 129,103 113,106 115,122 98,118 94,134 79,125 70,138 61,125 46,134 42,118 25,122 27,106 11,103 19,89 4,81 16,70 4,59 19,51 11,37 27,34 25,18 42,22 46,6 61,15"/>
      <circle cx="70" cy="70" r="50" fill="var(--white)"/>
    </svg>
    <div class="variety-badge-text">LABEL</div>

    <ul class="claims">
      <li class="claim"><svg class="claim-tick" viewBox="0 0 34 30"><path d="M3 16 L12 26 L31 4" fill="none" stroke="var(--white)" stroke-width="5" stroke-linecap="round" stroke-linejoin="round"/></svg>NO Egg</li>
      <li class="claim"><svg class="claim-tick" viewBox="0 0 34 30"><path d="M3 16 L12 26 L31 4" fill="none" stroke="var(--white)" stroke-width="5" stroke-linecap="round" stroke-linejoin="round"/></svg>NO Yeast</li>
      <li class="claim"><svg class="claim-tick" viewBox="0 0 34 30"><path d="M3 16 L12 26 L31 4" fill="none" stroke="var(--white)" stroke-width="5" stroke-linecap="round" stroke-linejoin="round"/></svg>NO Shortening</li>
      <li class="claim"><svg class="claim-tick" viewBox="0 0 34 30"><path d="M3 16 L12 26 L31 4" fill="none" stroke="var(--white)" stroke-width="5" stroke-linecap="round" stroke-linejoin="round"/></svg>NO Preservatives</li>
    </ul>

    <div class="origin-stamp">
      <div class="origin-leaf" role="img" aria-label="Canadian maple leaf"></div>
      <p class="origin-text">From Canadian<br>nature to your table</p>
    </div>

    <div class="info-band">
      <div class="cook-time">
        <svg class="microwave-icon" viewBox="0 0 54 36" aria-hidden="true">
          <rect x="2" y="2" width="50" height="32" rx="3" fill="none" stroke="var(--white)" stroke-width="3"/>
          <rect x="8" y="8" width="30" height="20" rx="2" fill="none" stroke="var(--white)" stroke-width="2.5"/>
          <line x1="45" y1="10" x2="45" y2="14" stroke="var(--white)" stroke-width="2.5"/>
          <line x1="45" y1="19" x2="45" y2="27" stroke="var(--white)" stroke-width="2.5"/>
          <path d="M20 22 q-3 -4 0 -8 M26 22 q-3 -4 0 -8" fill="none" stroke="var(--white)" stroke-width="2"/>
        </svg>
        <span class="cook-minutes">2</span>
        <span class="cook-label">min<br>microwave</span>
      </div>
      <p class="piece-count"><strong>6</strong> pieces</p>
    </div>
  </section>
</div>
</body>
</html>
```